We want a business card/punch card for our business. We are including examples of our current business card (we like the front of our business card and not looking to remake it). We need only back side to be designed in form of a punch card (we are including a sample of the punch card we made, but are unsatisfied). For each $180 spend (9 punches) our clients have $20 off.

Colors
886aae

```html
<!DOCTYPE html>
<html lang="en">
<head>
<meta charset="utf-8">
<title>Punch Card – Front and Back</title>
<link rel="stylesheet" href="https://fonts.googleapis.com/css2?family=Questrial&display=swap">
<style>
  :root {
    --page: #ffffff;
    --card-light: #95be4f;
    --card-dark: #7ba23a;
    --shadow: #b3b3b3;
    --ink-light: #efefef;
    --punch-fill: #ececec;
    --punch-ink: #8cbf4a;
    --badge-fill: #a0c468;
    --badge-ink: #8fbb4c;
  }
  * { margin: 0; padding: 0; box-sizing: border-box; }
  html, body {
    width: 1200px;
    height: 1200px;
    overflow: hidden;
    background: var(--page);
  }
  .canvas {
    position: relative;
    width: 1200px;
    height: 1200px;
  }
  .card-shadow {
    position: absolute;
    width: 810px;
    height: 479px;
    background: var(--shadow);
  }
  .card-shadow--front { left: 192px; top: 106px; }
  .card-shadow--back { left: 190px; top: 632px; }
  .card {
    position: absolute;
    width: 805px;
    height: 483px;
    overflow: hidden;
  }
  .card--front { left: 205px; top: 88px; }
  .card--back { left: 201px; top: 618px; }
  .card svg { display: block; width: 100%; height: 100%; }
  .card-base { fill: var(--card-light); }
  .card-wave { fill: var(--card-dark); }
  .service-list {
    font-family: "Questrial", "Century Gothic", sans-serif;
    font-size: 40px;
    fill: var(--ink-light);
  }
  .divider { fill: var(--ink-light); }
  .punch { fill: var(--punch-fill); }
  .punch-label {
    font-family: "Questrial", "Century Gothic", sans-serif;
    font-size: 22px;
    fill: var(--punch-ink);
    text-anchor: middle;
  }
  .reward-badge { fill: var(--badge-fill); }
  .reward-label {
    font-family: "Questrial", "Century Gothic", sans-serif;
    font-size: 122px;
    fill: var(--badge-ink);
    text-anchor: middle;
  }
</style>
</head>
<body>
<main class="canvas">
  <div class="card-shadow card-shadow--front"></div>
  <section class="card card--front" aria-label="Punch card with services">
    <svg viewBox="0 0 1006 604" preserveAspectRatio="none">
      <rect class="card-base" width="1006" height="604"/>
      <path class="card-wave" d="M0 604 C90 490 220 432 364 432 C440 432 490 442 540 455 C580 462 610 460 640 460 C790 460 920 400 1006 310 L1006 604 Z"/>
      <g class="service-list">
        <text x="86" y="180">Tantra</text>
        <text x="86" y="230">Intomacy Coaching</text>
        <text x="86" y="282">Sound Healing</text>
        <text x="86" y="335">Sound Baths</text>
        <text x="86" y="395">Crystal Healing</text>
        <text x="86" y="447">Yoga</text>
      </g>
      <rect class="divider" x="533" y="90" width="7" height="426"/>
      <g class="punch-grid">
        <circle class="punch" cx="680" cy="211" r="33"/><text class="punch-label" x="680" y="219">$20</text>
        <circle class="punch" cx="786" cy="211" r="33"/><text class="punch-label" x="786" y="219">$20</text>
        <circle class="punch" cx="886" cy="211" r="33"/><text class="punch-label" x="886" y="219">$20</text>
        <circle class="punch" cx="680" cy="302" r="33"/><text class="punch-label" x="680" y="310">$20</text>
        <circle class="punch" cx="786" cy="302" r="33"/><text class="punch-label" x="786" y="310">$20</text>
        <circle class="punch" cx="886" cy="302" r="33"/><text class="punch-label" x="886" y="310">$20</text>
        <circle class="punch" cx="680" cy="393" r="33"/><text class="punch-label" x="680" y="401">$20</text>
        <circle class="punch" cx="786" cy="393" r="33"/><text class="punch-label" x="786" y="401">$20</text>
        <circle class="punch" cx="886" cy="393" r="33"/><text class="punch-label" x="886" y="401">$20</text>
      </g>
    </svg>
  </section>

  <div class="card-shadow card-shadow--back"></div>
  <section class="card card--back" aria-label="Reward side">
    <svg viewBox="0 0 1006 604" preserveAspectRatio="none">
      <rect class="card-base" width="1006" height="604"/>
      <path class="card-wave" d="M0 604 C90 490 220 432 364 432 C440 432 490 442 540 455 C580 462 610 460 640 460 C790 460 920 400 1006 310 L1006 604 Z"/>
      <circle class="reward-badge" cx="503" cy="274" r="157"/>
      <text class="reward-label" x="503" y="314">$20</text>
    </svg>
  </section>
</main>
</body>
</html>
```